KFZ-Gutachter Banner

Ziel des Banners:
Der Banner soll auf die Tätigkeit als Kfz-Sachverständiger aufmerksam machen. Er wird im Außenbereich eingesetzt und soll schon aus der Ferne verständlich und gut lesbar sein.

Gestaltung:
• Schlichtes, professionelles Design (keine überladene Gestaltung, ruhige Farbwahl – anlehnend an den Farben schwarz und Rot.
• Ein Bild wo sich zwei hochwertige Autos verunfallt befinden
• Großzügige Schriftgrößen – der Text muss auch aus 20–30 m Entfernung gut lesbar sein
• Klare Informationsstruktur

Inhalte (Text):
1. Überschrift / Hauptaussage (groß & auffällig):
Kfz-Sachverständiger
oder
Unfallgutachten vom Profi
2. Kurze Beschreibung (kleiner, aber lesbar):
• Unfallgutachten
• Fahrzeugbewertung
• Technische Beratung
3. Kontaktdaten (am wichtigsten – sehr gut sichtbar & lesbar):
• Telefonnummer (z. B. groß & fett)
• Website oder E-Mail
• Optional: Standort oder “auch mobil im Einsatz”

Bildelemente:
• Optional ein dezentes Symbol oder Icon (z. B. Auto, Lupe, Checkzeichen) – nur wenn es nicht vom Text ablenkt

Format:
• Querformat, je nach Platz vor Ort (z. B. 3 m x 1,5 m)

Ingenieurbüro Lorenz Vahle Ostlinger Str.14 58706 Menden www.pruefwerk-tz.de

• Man muss sofort erkennen, dass es sich um einen KFZ-Gutachter handelt.

```html
<!DOCTYPE html>
<html lang="de">
<head>
<meta charset="utf-8">
<title>Lorenz Vahle – Kfz-Sachverständiger Banner</title>
<link href="https://fonts.googleapis.com/css2?family=Outfit:wght@400;500;800&display=swap" rel="stylesheet">
<style>
  :root {
    --black: #000000;
    --ink: #0a0a0a;
    --white: #ffffff;
    --red: #ff0000;
    --red-deep: #e60000;
    --steel-light: #c9ccd0;
    --steel-mid: #8c9096;
    --steel-dark: #2b2d31;
  }
  * { margin: 0; padding: 0; box-sizing: border-box; }
  html, body {
    width: 1200px; height: 714px; overflow: hidden;
    background: var(--black);
    font-family: "Outfit", sans-serif;
  }
  .banner {
    position: absolute; left: 125px; top: 119px;
    width: 950px; height: 475px;
    background: var(--white);
    overflow: hidden;
  }
  .banner-art { position: absolute; inset: 0; }
  .brand {
    position: absolute; left: 46px; top: 45px;
    display: flex; align-items: center; gap: 19px;
  }
  .brand-square {
    width: 69px; height: 69px;
    border: 3px solid var(--ink);
    border-radius: 4px;
  }
  .brand-name {
    font-size: 27px; font-weight: 400; letter-spacing: 3px;
    color: var(--ink); line-height: 1;
  }
  .brand-tag {
    margin-top: 6px;
    font-size: 12.5px; font-weight: 400; letter-spacing: 2.2px;
    color: var(--ink); line-height: 16px;
  }
  .headline {
    position: absolute; left: 46px; top: 136px;
    font-size: 44px; font-weight: 800; line-height: 44px;
    color: var(--ink); letter-spacing: 0.5px;
  }
  .services { position: absolute; left: 48px; top: 249px; }
  .service {
    position: absolute; left: 0; height: 32px;
    padding-left: 3px;
    font-size: 28px; font-weight: 400; line-height: 30px;
    color: var(--white); white-space: nowrap;
  }
  .service--red-black { background: linear-gradient(90deg, var(--red) 0%, var(--black) 100%); }
  .service--black-red { background: linear-gradient(90deg, var(--black) 0%, var(--red) 100%); }
  .service-1 { top: 0; width: 231px; }
  .service-2 { top: 44px; width: 279px; }
  .service-3 { top: 87px; width: 291px; }
  .phone {
    position: absolute; left: 52px; top: 380px;
    font-size: 35px; font-weight: 800; color: var(--ink); line-height: 40px;
  }
  .website {
    position: absolute; left: 53px; top: 419px;
    font-size: 19px; font-weight: 500; color: var(--ink); line-height: 22px;
  }
</style>
</head>
<body>
  <section class="banner">
    <svg class="banner-art" width="950" height="475" viewBox="0 0 950 475">
      <defs>
        <linearGradient id="crash-photo-tone" x1="0" y1="0" x2="0.3" y2="1">
          <stop offset="0" stop-color="var(--steel-light)"/>
          <stop offset="0.45" stop-color="var(--steel-mid)"/>
          <stop offset="1" stop-color="var(--steel-dark)"/>
        </linearGradient>
      </defs>
      <polygon class="accent-wedge" fill="var(--red)"
        points="558,0 580,0 509,256 539,475 519,475 505,256"/>
      <polygon class="crash-photo" fill="url(#crash-photo-tone)"
        role="img" aria-label="Foto: zwei silberne Autos nach einem Frontalzusammenstoß vor einer grauen Betonwand"
        points="580,0 950,0 950,475 539,475 509,256"/>
    </svg>

    <div class="brand">
      <div class="brand-square"></div>
      <div class="brand-text">
        <div class="brand-name">LORENZ VAHLE</div>
        <div class="brand-tag">KFZ-SACHVERSTÄNDIGER<br>INGENIEURBÜRO</div>
      </div>
    </div>

    <h1 class="headline">UNFALLGUTACHTEN<br>VOM PROFI</h1>

    <ul class="services">
      <li class="service service-1 service--red-black">Unfallgutachten</li>
      <li class="service service-2 service--black-red">Fahrzeugbewertung</li>
      <li class="service service-3 service--red-black">Technische Beratung</li>
    </ul>

    <p class="phone">+49 170 58204716</p>
    <p class="website">www.vahle-gutachten.de</p>
  </section>
</body>
</html>
```